Amber Hollow Productions

I need a business card design for a new freelance film production company using or incorporating the logo:
I want the card to be creative, minimal, yet professional. Feel free to use a variety of different shapes and sizes/ textures for the card.

Industry/Entity Type

Film Production

```html
<!DOCTYPE html>
<html lang="en">
<head>
<meta charset="UTF-8">
<title>Amber Hollow Productions Business Card</title>
<link rel="stylesheet" href="https://fonts.googleapis.com/css2?family=Montserrat:wght@400;500;700&display=swap">
<style>
  :root {
    --brand-blue: #1f5fb3;
    --brand-blue-deep: #174f9c;
    --card-white: #ffffff;
    --ink: #1d1d1f;
    --stage: #cfd0d0;
  }
  * { margin: 0; padding: 0; box-sizing: border-box; }
  html, body {
    width: 1200px;
    height: 861px;
    overflow: hidden;
    background: var(--stage);
    font-family: "Montserrat", Arial, sans-serif;
  }
  .sheet {
    width: 1200px;
    height: 861px;
    display: flex;
    align-items: center;
    justify-content: center;
    gap: 64px;
  }
  .card {
    background: var(--card-white);
    box-shadow: 0 6px 18px rgba(0,0,0,0.18);
    position: relative;
    overflow: hidden;
  }

  /* Front */
  .card-front {
    width: 340px;
    height: 595px;
  }
  .front-wash {
    position: absolute;
    inset: 0;
    background: linear-gradient(180deg,
      var(--card-white) 0%,
      var(--card-white) 11%,
      var(--brand-blue) 11%,
      var(--brand-blue) 38%,
      rgba(31,95,179,0.55) 52%,
      rgba(255,255,255,0) 66%);
  }
  .front-texture {
    position: absolute;
    right: 0;
    top: 66px;
    width: 150px;
    height: 300px;
    background: linear-gradient(100deg, rgba(255,255,255,0) 0%, rgba(255,255,255,0.35) 60%, rgba(255,255,255,0.7) 100%);
  }
  .front-brand {
    position: absolute;
    top: 92px;
    left: 0;
    right: 0;
    text-align: center;
    color: var(--card-white);
    font-weight: 500;
    font-size: 26px;
    letter-spacing: 1px;
    text-transform: uppercase;
    line-height: 1.15;
  }
  .front-person {
    position: absolute;
    top: 218px;
    left: 0;
    right: 0;
    text-align: center;
    color: var(--card-white);
  }
  .person-name {
    font-weight: 700;
    font-size: 23px;
    letter-spacing: 0.5px;
  }
  .person-role {
    font-weight: 500;
    font-size: 15px;
    margin-top: 2px;
  }
  .contact-list {
    position: absolute;
    top: 338px;
    left: 40px;
    right: 20px;
    list-style: none;
  }
  .contact-item {
    display: flex;
    align-items: center;
    gap: 12px;
    color: var(--ink);
    font-size: 15px;
    line-height: 1.1;
    margin-bottom: 13px;
  }
  .contact-icon {
    flex: 0 0 22px;
    width: 22px;
    height: 22px;
  }

  /* Back */
  .card-back {
    width: 595px;
    height: 340px;
    display: flex;
    align-items: center;
    justify-content: center;
  }
  .back-brand {
    color: var(--brand-blue);
    font-weight: 500;
    font-size: 44px;
    letter-spacing: 2px;
    text-transform: uppercase;
    text-align: center;
    line-height: 1.15;
  }
</style>
</head>
<body>
<main class="sheet">
  <section class="card card-front" aria-label="Business card front">
    <div class="front-wash"></div>
    <div class="front-texture" role="img" aria-label="Soft frosted texture fading the blue band into white"></div>
    <div class="front-brand">Amber Hollow<br>Productions</div>
    <div class="front-person">
      <div class="person-name">NAME SURNAME</div>
      <div class="person-role">Position</div>
    </div>
    <ul class="contact-list">
      <li class="contact-item">
        <svg class="contact-icon" viewBox="0 0 22 22"><circle cx="11" cy="11" r="11" fill="var(--brand-blue)"/><path d="M11 5a4 4 0 0 0-4 4c0 3 4 8 4 8s4-5 4-8a4 4 0 0 0-4-4z" fill="#fff"/><circle cx="11" cy="9" r="1.5" fill="var(--brand-blue)"/></svg>
        <span>12 Lorem Street, Ipsum City,<br>Dolor Sit Amet</span>
      </li>
      <li class="contact-item">
        <svg class="contact-icon" viewBox="0 0 22 22"><circle cx="11" cy="11" r="11" fill="var(--brand-blue)"/><path d="M7 6l2.5-.5 1.2 3-1.4 1a7 7 0 0 0 3.2 3.2l1-1.4 3 1.2L16 15c-5 .5-9.5-4-9-9z" fill="#fff"/></svg>
        <span>+1234-5678-9000</span>
      </li>
      <li class="contact-item">
        <svg class="contact-icon" viewBox="0 0 22 22"><circle cx="11" cy="11" r="11" fill="var(--brand-blue)"/><rect x="8" y="5" width="6" height="12" rx="1" fill="#fff"/><rect x="9" y="7" width="4" height="6" fill="var(--brand-blue)"/></svg>
        <span>+1234-5678-9123</span>
      </li>
      <li class="contact-item">
        <svg class="contact-icon" viewBox="0 0 22 22"><circle cx="11" cy="11" r="11" fill="var(--brand-blue)"/><rect x="5" y="7" width="12" height="8" fill="#fff"/><path d="M5 7l6 5 6-5" fill="none" stroke="var(--brand-blue)" stroke-width="1.2"/></svg>
        <span>youremail@website.com</span>
      </li>
      <li class="contact-item">
        <svg class="contact-icon" viewBox="0 0 22 22"><circle cx="11" cy="11" r="11" fill="var(--brand-blue)"/><g fill="none" stroke="#fff" stroke-width="1.2"><circle cx="11" cy="11" r="6"/><ellipse cx="11" cy="11" rx="2.6" ry="6"/><path d="M5 11h12M6 8h10M6 14h10"/></g></svg>
        <span>www.yourwebsite.com</span>
      </li>
      <li class="contact-item">
        <svg class="contact-icon" viewBox="0 0 22 22"><circle cx="11" cy="11" r="11" fill="var(--brand-blue)"/></svg>
        <span>amberhollowproductions</span>
      </li>
    </ul>
  </section>

  <section class="card card-back" aria-label="Business card back">
    <div class="back-brand">Amber Hollow<br>Productions</div>
  </section>
</main>
</body>
</html>
```